Need a tea box packaging design

* Organic Herbal tea
* Imported from india to france for european community
* our main rivals are " ZENDRA" tea and " BRAVO" tea.
* the product will be sold online and shops.
* 15 variety of teas will be imported.
* The details in the attached file.
The Packaging contents:
Main page :
Brand Name : KORIL ( logo attached)
Name of the product: KELORA THE NOIR ( which means Kelora black tea)
Type of the product : Infusion
No of tea bags : 20
Weight of each bag : 1,5 gm
Total weight : 30 gm
Organic label name : Europe ( organic logo attached)
vegan label : vegan ( vegan label attached)
The other side contents will be given later.
A model that i have designed with another designer is attached. It is nice. But i am expecting more than that. ( attached)
Some designs that i like are attached here.
As mentionned earlier there will 15 variety of teas, so the design should easily modifiable by just changing colours.
Updates
Project Deadline Extended Reason: I think the deadline is very short due to the weekend. So, I feel it is better to extend the deadline by 5 days. Added Saturday, January 21, 2017
Target Market(s)
Europe. Mainly france.
Industry/Entity Type
Community
Requirements
Must have
- * Design should be modern and colourfull.
- * I like pattern works, Vectorials
- * Yoga silouhaites in the design is appreciable.
- * The design should express wellness, joy and love
Nice to have
- "Zendra" tea in my inspirational design.
- * The ingredients can be showed in vectorial designs in the back ground.
- * The end user must see the box while taking the tea and appreciate
- * The end user must search and find some hidden things.
- * The box must be communicative.
- * Trendy frames.
Should not have
- No need to have tea cups

```html
<!DOCTYPE html>
<html lang="en">
<head>
<meta charset="utf-8">
<title>Koril – Kelora Infusion Packaging</title>
<link rel="stylesheet" href="https://fonts.googleapis.com/css2?family=Cinzel:wght@400;500&display=swap">
<style>
  :root {
    --backdrop: #dde1e4;
    --kraft: #e8e2d3;
    --kraft-deep: #d6cdb9;
    --line-art: #a9a497;
    --line-art-soft: #c4beb0;
    --ink: #141414;
    --brand: #a3652c;
    --green-tint: #a6d495;
    --green-splash: #b9dcae;
    --amber-tint: #e3a856;
    --amber-splash: #ecc089;
  }
  * { box-sizing: border-box; margin: 0; padding: 0; }
  html, body {
    width: 1200px; height: 1069px; overflow: hidden;
    background: var(--backdrop);
    font-family: "Cinzel", "Times New Roman", serif;
    color: var(--ink);
  }
  .range {
    position: absolute; top: 227px; left: 170px;
    display: flex; gap: 60px;
  }
  .box-front {
    position: relative; width: 400px; height: 615px;
    background: var(--kraft);
    overflow: hidden;
  }
  .botanical-art {
    position: absolute; inset: 0;
    background:
      radial-gradient(ellipse 110px 70px at 120px 560px, var(--splash) 0%, transparent 70%),
      radial-gradient(ellipse 70px 50px at 310px 150px, var(--splash) 0%, transparent 75%),
      radial-gradient(ellipse 90px 60px at 320px 575px, var(--splash) 0%, transparent 70%),
      radial-gradient(ellipse 130px 80px at 200px 120px, var(--line-art-soft) 0%, transparent 72%),
      radial-gradient(ellipse 210px 90px at 200px 560px, var(--line-art) 0%, var(--line-art-soft) 40%, transparent 78%),
      radial-gradient(ellipse 60px 190px at 30px 370px, var(--line-art-soft) 0%, transparent 75%),
      radial-gradient(ellipse 70px 180px at 370px 330px, var(--line-art-soft) 0%, transparent 75%),
      radial-gradient(ellipse 60px 40px at 340px 480px, #f4f1ea 0%, transparent 80%);
  }
  .green { --tint: var(--green-tint); --splash: var(--green-splash); }
  .amber { --tint: var(--amber-tint); --splash: var(--amber-splash); }
  .brand-name {
    position: absolute; top: 14px; left: 0; width: 100%;
    text-align: center; font-size: 26px; font-weight: 400;
    letter-spacing: 4px; color: var(--brand);
  }
  .flavour-tile {
    position: absolute; left: 68px; top: 158px; width: 259px; height: 310px;
    background: var(--tint); opacity: .92;
  }
  .label-frame {
    position: absolute; left: 60px; top: 146px; width: 283px; height: 330px;
    border: 2px solid var(--ink);
  }
  .label-content {
    position: absolute; left: 68px; top: 158px; width: 259px; height: 310px;
    text-align: center;
  }
  .pot-icon { position: absolute; left: 109px; top: 22px; width: 42px; height: 42px; }
  .rule { position: absolute; left: 80px; width: 99px; height: 2px; background: var(--ink); }
  .rule-top { top: 78px; }
  .rule-bottom { top: 194px; }
  .product-name {
    position: absolute; top: 96px; left: 0; width: 100%;
    font-size: 62px; font-weight: 400; line-height: 1; letter-spacing: 1px;
  }
  .product-type {
    position: absolute; top: 216px; left: 0; width: 100%;
    font-size: 20px; line-height: 1.05; letter-spacing: 1px; color: #2a2a2a;
  }
</style>
</head>
<body>
<main class="range">
  <section class="box-front green">
    <div class="botanical-art" role="img" aria-label="Hand-drawn line illustration of lilies, frangipani, roses and fern leaves framing the label, with soft green watercolour splashes"></div>
    <div class="brand-name">KORIL</div>
    <div class="flavour-tile"></div>
    <div class="label-frame"></div>
    <div class="label-content">
      <svg class="pot-icon" viewBox="0 0 42 42" aria-hidden="true">
        <circle cx="21" cy="8" r="3" fill="#141414"/>
        <path d="M8 14 H34 L32 32 Q21 37 10 32 Z" fill="#141414"/>
        <path d="M34 18 Q41 19 38 26 L33 28" fill="none" stroke="#141414" stroke-width="2.5"/>
        <path d="M9 20 L2 14 L4 13 L10 17" fill="#141414"/>
      </svg>
      <div class="rule rule-top"></div>
      <h1 class="product-name">KELORA</h1>
      <div class="rule rule-bottom"></div>
      <p class="product-type">Green Tea<br>Infusion</p>
    </div>
  </section>

  <section class="box-front amber">
    <div class="botanical-art" role="img" aria-label="Hand-drawn line illustration of lilies, frangipani, roses and fern leaves framing the label, with soft orange watercolour splashes"></div>
    <div class="brand-name">KORIL</div>
    <div class="flavour-tile"></div>
    <div class="label-frame"></div>
    <div class="label-content">
      <svg class="pot-icon" viewBox="0 0 42 42" aria-hidden="true">
        <circle cx="21" cy="5" r="2.5" fill="#141414"/>
        <path d="M15 9 H27 Q31 20 27 30 H15 Q11 20 15 9 Z" fill="#141414"/>
        <rect x="13" y="31" width="16" height="4" fill="#141414"/>
        <path d="M27 13 Q36 14 31 24" fill="none" stroke="#141414" stroke-width="2.5"/>
        <path d="M15 14 L6 9 L7 7 L15 11" fill="#141414"/>
      </svg>
      <div class="rule rule-top"></div>
      <h1 class="product-name">KELORA</h1>
      <div class="rule rule-bottom"></div>
      <p class="product-type">Roibos<br>Infusion</p>
    </div>
  </section>
</main>
</body>
</html>
```